National online rug retailer needs a home page design

See the MatsNowly logo and create a home page design around that color theme. Details are spelled out in word document uploaded below.

Apparently this website did not take my attachement showing the logo and basic requirements.  If you would send me your email address, I will send you the attachment directly.
Best regards,
Ned Ferris
nferris@qorvex.com

Target Market(s)

The target market is home owners 25 to 75 years old with combined incomes over $100,000 per year.

Industry/Entity Type

Online

Requirements
Must have
• Lots of white space with black letters and creative use of red and possibly one other color. Would like a compelling call to action button.

```html
<!DOCTYPE html>
<html lang="en">
<head>
<meta charset="utf-8">
<title>MatsNowly – Home</title>
<link href="https://fonts.googleapis.com/css2?family=Source+Sans+3:ital,wght@0,400;0,600;0,700;1,400&family=Oswald:wght@500&display=swap" rel="stylesheet">
<style>
:root{
  --red:#d71920;
  --red-dark:#a80f14;
  --ink:#2b2b2b;
  --grey:#666;
  --muted:#9a9a9a;
  --line:#dcdcdc;
  --carpet:#e6ddd2;
  --carpet-light:#f3eee8;
  --nav-top:#5a5a5a;
  --nav-bottom:#262626;
  --footer-bg:#f6f3ef;
  --bottom-bar:#2e2e2e;
}
*{box-sizing:border-box;margin:0;padding:0}
html,body{width:847px;height:1200px;overflow:hidden}
body{position:relative;background:#fff;font-family:"Source Sans 3",Arial,sans-serif;color:var(--ink);font-size:11px}
.abs{position:absolute}
.carpet-bg{left:0;top:0;width:847px;height:540px;background:linear-gradient(180deg,var(--carpet) 0%,#ece5dc 70%,#fff 100%)}
.topbar{top:14px;left:486px;font-size:9.5px;letter-spacing:-.2px;display:flex;gap:18px;color:var(--ink)}
.checkout{left:684px;top:10px;width:70px;height:20px;background:var(--red);border:1px solid var(--red-dark);border-radius:3px;color:#fff;font-size:9.5px;font-weight:600;display:flex;align-items:center;justify-content:center;gap:3px}
.logo{left:92px;top:24px;display:flex;align-items:center;gap:6px}
.logo .mark{width:12px;height:12px;background:var(--red)}
.logo .name{font-size:30px;font-weight:400;color:var(--red);letter-spacing:-1px;line-height:1}
.tagline{left:157px;top:66px;font-size:9px;color:var(--grey)}
.search{left:316px;top:54px;width:228px;height:18px;background:#fff;border:1px solid #ccc;font-size:8px;color:var(--muted);padding:3px 8px;display:flex;justify-content:space-between}
.account{left:562px;top:58px;font-size:8.5px;color:var(--ink)}
.chat{left:663px;top:52px;font-size:9px;line-height:15px}
.chat .online{color:#5fb02c;display:flex;align-items:center;gap:3px}
.chat .dot{width:8px;height:8px;border-radius:50%;background:#5fb02c}
.agent{left:708px;top:36px;width:44px;height:52px;background:linear-gradient(180deg,#d9c2b0,#f4f4f4);border-radius:4px}
.nav{left:92px;top:90px;width:662px;height:28px;background:linear-gradient(180deg,var(--nav-top),var(--nav-bottom));border:2px solid #bbb;border-radius:3px;display:flex;align-items:center;justify-content:space-around;color:#fff;font-size:11px}
.nav span+span{border-left:1px solid #6a6a6a;padding-left:16px}
.browse{left:92px;top:126px;font-size:15px;color:#444;letter-spacing:-.3px}
.tollfree{left:590px;top:127px;font-size:12.5px;color:var(--muted);letter-spacing:-.4px}
.tollfree b{color:var(--red);font-weight:400}
.sidebar{left:94px;top:153px;width:159px;height:345px;background:#f1f1f1;border:3px solid #fff;box-shadow:0 0 3px rgba(0,0,0,.15);padding:6px 10px;font-style:italic;color:#777}
.sidebar .h{font-size:11px;padding:3px 2px;border-bottom:1px dotted #ccc;height:23.5px;display:flex;align-items:center}
.sidebar .s{font-size:9px;color:var(--muted);padding-left:10px;height:17.3px;border-bottom:1px solid #e2e2e2;display:flex;align-items:center}
.hero{left:266px;top:153px;width:488px;height:228px;border:3px solid #555;background:linear-gradient(180deg,#eee5d6 0%,#f7f1e6 55%,#3b2a22 85%,#2a1c16 100%)}
.also{left:266px;top:393px;font-size:12px;font-weight:600;color:#444}
.thumb{top:412px;width:102px;height:86px;border:4px solid #9a9a9a}
.arrow{top:441px}
.divider{left:150px;top:518px;width:545px;border-top:1px dotted #ccc}
.promo{left:92px;top:534px;width:664px;height:59px;border:1px solid #ccc;background:#fff}
.promo .pan{left:0;top:0;width:100px;height:57px;background:linear-gradient(135deg,#d8d8d8,#3a3a3a)}
.promo .tag{left:101px;top:1px;width:28px;height:28px;background:#f06a1c;color:#fff;font-size:6px;text-align:center;line-height:7px;padding-top:3px}
.promo .title{left:141px;top:14px;font-family:"Oswald",sans-serif;font-size:15px;color:#222}
.promo .sub{left:141px;top:32px;font-size:10.5px;color:#333}
.promo .price{left:330px;top:21px;font-size:9px}
.promo .price b{font-size:15px}
.buy{left:404px;top:25px;width:62px;height:16px;background:#f06a1c;border-radius:2px;color:#fff;font-size:8px;font-weight:700;display:flex;align-items:center;justify-content:center}
.promo .perks{left:485px;top:25px;font-size:6px;font-weight:700;color:#555;line-height:8px}
.promo .shop{left:595px;top:16px;font-size:12px;font-style:italic;color:var(--red)}
.featured{left:92px;top:606px;font-size:14px;color:#333;letter-spacing:-.3px}
.featured-line{left:212px;top:617px;width:542px;border-top:1px solid #e5e5e5}
.card{width:120px}
.card .img{height:97px;border:4px solid #a0a0a0}
.card h3{margin-top:9px;font-size:11.5px;font-weight:400;color:var(--red)}
.card p{font-size:7.5px;color:var(--muted);line-height:10.5px;margin-top:2px}
.footer{left:0;top:968px;width:847px;height:186px;background:var(--footer-bg)}
.fcol h4{font-size:12px;font-weight:400;color:var(--red);margin-bottom:14px}
.fcol ul{list-style:none;font-size:8.5px;color:#666;line-height:13px}
.fsep{top:990px;height:140px;border-left:1px solid #e3ddd6}
.signup h4{font-size:10.5px;font-weight:400;color:var(--red);line-height:12px}
.email{left:572px;top:1014px;width:183px;height:21px;border:1px solid #bbb;border-radius:2px;background:#fff;font-size:7.5px;color:var(--muted);padding:5px 9px}
.submit{left:704px;top:1043px;width:50px;height:18px;background:var(--red);color:#fff;font-size:8px;font-weight:700;display:flex;align-items:center;justify-content:center;border-radius:2px}
.card-pay{width:24px;height:14px;background:#d7d7d7;border:1px solid #bbb}
.badge{background:#d9d0b0;border-radius:50%}
.bottom{left:0;top:1154px;width:847px;height:46px;background:var(--bottom-bar)}
.copy{left:92px;top:1171px;font-size:9.5px;color:#ddd}
.bottom-logo{left:640px;top:1165px;display:flex;align-items:center;gap:4px;font-size:17px;color:#777}
.bottom-logo .mark{width:8px;height:8px;background:#777}
</style>
</head>
<body>
<div class="abs carpet-bg" role="img" aria-label="Soft beige shag carpet background"></div>

<div class="abs topbar"><span>ITEMS: 12</span><span>TOTAL: $0.00</span><span>VIEW CART</span></div>
<div class="abs checkout">
  <svg width="8" height="8" viewBox="0 0 8 8"><circle cx="4" cy="4" r="4" fill="#fff"/><path d="M3 2l3 2-3 2z" fill="#d71920"/></svg>CHECKOUT
</div>

<div class="abs logo"><span class="mark"></span><span class="name">MatsNowly.com</span></div>
<div class="abs tagline">for domestic and heirloom values</div>

<div class="abs search"><span>Enter key words or item #</span>
  <svg width="10" height="10" viewBox="0 0 10 10"><circle cx="4" cy="4" r="3" fill="none" stroke="#555" stroke-width="1.4"/><path d="M6.3 6.3L9 9" stroke="#555" stroke-width="1.6"/></svg>
</div>
<div class="abs account">My Account &nbsp;|&nbsp; Sign In</div>
<div class="abs chat">LIVE CHAT<div class="online"><span class="dot"></span>Online</div></div>
<div class="abs agent" role="img" aria-label="Customer support agent with headset"></div>

<nav class="abs nav"><span>Home</span><span>Selection Guides</span><span>Rug Care</span><span>FAQ</span><span>Return Policy</span><span>Free Shipping</span><span>Clearance Rugs</span></nav>

<div class="abs browse">BROWSE</div>
<div class="abs tollfree">
  <svg width="8" height="12" viewBox="0 0 8 12"><path d="M6 1C2 1 1 4 1 6s1 5 5 5" fill="none" stroke="#d71920" stroke-width="2"/></svg>
  Order Toll-Free: <b>1-888-555-0142</b>
</div>

<aside class="abs sidebar">
  <div class="h">Rug Theme ::::</div>
  <div class="s">Traditional</div><div class="s">Transitional</div><div class="s">Casual</div>
  <div class="h">Color Way ::::</div>
  <div class="s">Black</div><div class="s">Blue</div><div class="s">Green</div><div class="s">Gold</div>
  <div class="h">Size ::::</div>
  <div class="h">Shape ::::</div>
  <div class="h">Fiber Content ::::</div>
  <div class="h">MFGR. Brand ::::</div>
  <div class="h">MFGR. Collection ::::</div>
  <div class="h">Price ::::</div>
</aside>

<div class="abs hero" role="img" aria-label="Cream fur shag rug on dark wood floor"></div>
<div class="abs also">You May Also Like:</div>
<svg class="abs arrow" style="left:268px" width="10" height="20" viewBox="0 0 10 20"><path d="M10 0L0 10l10 10z" fill="#e24a4a"/></svg>
<div class="abs thumb" style="left:288px;background:linear-gradient(160deg,#c9b08f,#f1ebdd 60%,#5a3a28)" role="img" aria-label="Fur rug"></div>
<div class="abs thumb" style="left:400px;background:linear-gradient(160deg,#c9a889,#8b7a6a 50%,#c58a52)" role="img" aria-label="Modern pebble pattern rug"></div>
<div class="abs thumb" style="left:512px;background:linear-gradient(135deg,#c93a2a,#2e4a8a 50%,#e0a030)" role="img" aria-label="Traditional patterned rug"></div>
<div class="abs thumb" style="left:624px;background:linear-gradient(180deg,#e9eee3,#f6f6ef 60%,#c8c7a8)" role="img" aria-label="Rug in living room with sofa"></div>
<svg class="abs arrow" style="left:740px" width="10" height="20" viewBox="0 0 10 20"><path d="M0 0l10 10L0 20z" fill="#e24a4a"/></svg>
<div class="abs divider"></div>

<section class="abs promo">
  <div class="abs pan" role="img" aria-label="Frying pan and grill pan"></div>
  <div class="abs tag">UPTO<br><b style="font-size:7px">50%</b><br>off</div>
  <div class="abs title">KITCHEN SALE</div>
  <div class="abs sub">Largest selection of Kitchen Appliances</div>
  <div class="abs price">Starting ₹ <b>199</b></div>
  <div class="abs buy">Buy Now</div>
  <div class="abs perks">• MANUFACTURER WARRANTY<br>• FREE SHIPPING</div>
  <div class="abs shop">ShopDaily</div>
</section>

<div class="abs featured">Featured Products:</div>
<div class="abs featured-line"></div>

<div class="abs card" style="left:92px;top:630px"><div class="img" style="background:linear-gradient(160deg,#c9b08f,#f1ebdd 60%,#5a3a28)" role="img" aria-label="Fur rug"></div><h3>FUR RUGS</h3><p>Lorem Ipsum is simply dummy text of the printing and type...</p></div>
<div class="abs card" style="left:228px;top:630px"><div class="img" style="background:linear-gradient(160deg,#c9a889,#8b7a6a 50%,#c58a52)" role="img" aria-label="Modern rug"></div><h3>MODERN RUGS</h3><p>Lorem Ipsum is simply dummy text of the printing and type...</p></div>
<div class="abs card" style="left:364px;top:630px"><div class="img" style="background:linear-gradient(135deg,#c93a2a,#2e4a8a 50%,#e0a030)" role="img" aria-label="Traditional rug"></div><h3>TRADITIONAL RUGS</h3><p>Lorem Ipsum is simply dummy text of the printing and type...</p></div>
<div class="abs card" style="left:499px;top:630px"><div class="img" style="background:linear-gradient(180deg,#e9eee3,#f6f6ef 60%,#c8c7a8)" role="img" aria-label="Fancy rug in living room"></div><h3>FANCY RUGS</h3><p>Lorem Ipsum is simply dummy text of the printing and type...</p></div>
<div class="abs card" style="left:634px;top:630px"><div class="img" style="background:linear-gradient(160deg,#c9a889,#8b7a6a 50%,#c58a52)" role="img" aria-label="Casual rug"></div><h3>CASUAL RUGS</h3><p>Lorem Ipsum is simply dummy text of the printing and type...</p></div>

<div class="abs card" style="left:92px;top:787px"><div class="img" style="background:linear-gradient(160deg,#c9b08f,#f1ebdd 60%,#5a3a28)" role="img" aria-label="Fur rug"></div><h3>FUR RUGS</h3><p>Lorem Ipsum is simply dummy text of the printing and type...</p></div>
<div class="abs card" style="left:228px;top:787px"><div class="img" style="background:linear-gradient(160deg,#c9a889,#8b7a6a 50%,#c58a52)" role="img" aria-label="Modern rug"></div><h3>MODERN RUGS</h3><p>Lorem Ipsum is simply dummy text of the printing and type...</p></div>
<div class="abs card" style="left:364px;top:787px"><div class="img" style="background:linear-gradient(135deg,#c93a2a,#2e4a8a 50%,#e0a030)" role="img" aria-label="Traditional rug"></div><h3>TRADITIONAL RUGS</h3><p>Lorem Ipsum is simply dummy text of the printing and type...</p></div>
<div class="abs card" style="left:499px;top:787px"><div class="img" style="background:linear-gradient(180deg,#e9eee3,#f6f6ef 60%,#c8c7a8)" role="img" aria-label="Fancy rug in living room"></div><h3>FANCY RUGS</h3><p>Lorem Ipsum is simply dummy text of the printing and type...</p></div>
<div class="abs card" style="left:634px;top:787px"><div class="img" style="background:linear-gradient(160deg,#c9a889,#8b7a6a 50%,#c58a52)" role="img" aria-label="Casual rug"></div><h3>CASUAL RUGS</h3><p>Lorem Ipsum is simply dummy text of the printing and type...</p></div>

<footer class="abs footer"></footer>
<div class="abs fsep" style="left:232px"></div>
<div class="abs fsep" style="left:390px"></div>
<div class="abs fsep" style="left:552px"></div>
<div class="abs fcol" style="left:92px;top:983px"><h4>Customer Service</h4><ul><li>Shipping</li><li>Return Policy</li><li>Privacy Policy</li><li>Ordering &amp; Delivery Checklist</li><li>Terms of Use</li><li>Terms of Sale</li><li>Contact Us</li><li>Environmental Policy</li></ul></div>
<div class="abs fcol" style="left:272px;top:983px"><h4>Resources</h4><ul><li>Product Articles</li><li>Learning Center</li><li>Help</li><li>Refer A Friend</li><li>MatsNowly Blog</li><li>Room Scene Viewer</li><li>Site Map</li><li>FAQ</li><li>Customer Testimonials</li><li>Photo Gallery</li></ul></div>
<div class="abs fcol" style="left:420px;top:983px"><h4>Corporate Info</h4><ul style="margin-top:-2px"><li>About MatsNowly.com</li><li>Careers</li><li>Affiliates</li></ul></div>

<div class="abs card-pay" style="left:423px;top:1079px"></div>
<div class="abs card-pay" style="left:452px;top:1079px"></div>
<div class="abs card-pay" style="left:478px;top:1079px"></div>
<div class="abs card-pay" style="left:423px;top:1105px"></div>
<div class="abs card-pay" style="left:452px;top:1105px"></div>
<div class="abs card-pay" style="left:478px;top:1105px"></div>

<div class="abs signup" style="left:571px;top:984px"><h4>Sign up for Daily Fair Deals.<br>Don't miss out!</h4></div>
<div class="abs email">Enter Your Email Address</div>
<div class="abs submit">SUBMIT</div>
<div class="abs badge" style="left:610px;top:1072px;width:32px;height:32px"></div>
<div class="abs badge" style="left:664px;top:1074px;width:30px;height:30px"></div>
<div class="abs" style="left:704px;top:1078px;width:42px;height:18px;background:#e1e1e1;border:1px solid #bbb"></div>
<div class="abs" style="left:627px;top:1113px;width:46px;height:22px;background:#e6e6e6;border:1px solid #bbb"></div>
<div class="abs" style="left:682px;top:1112px;width:44px;height:24px;background:#d6dde8;border:1px solid #aab"></div>

<div class="abs bottom"></div>
<div class="abs copy">©1998-2013 MatsNowly.com Inc. All rights reserved.</div>
<div class="abs bottom-logo"><span class="mark"></span>MatsNowly.com</div>
</body>
</html>
```